E-Commerce Website Update for Bamboo Poles Company

Existing website at:

http://www.reedcraftstudio.example/
http://www.reedcraftstudio.example/pages/product-and-price-list

Two pages to design: home page and "price list" page.

Info for home page as follows:

HOME PAGE:

Header:
Company Name: reedcraft studio
Telephone: 1 888 412 5093

Across the top:
Home | Price List | Blog | FAQ | About | Contact

Down the side:
About Bamboo
Wedding Arbors
Bamboo For Flutes
Black Bamboo
Spotted Bamboo
Bamboo Carpentry
Photo Gallery
All Products & Prices
Blog
FAQ
About
Contact

Should have shopping cart and search buttons on top.
Please see ai file, attached for logo (leaf) and font
In addition the homepage should have one or two sections for promotions

Chosen design will be asked to help deign a PRODUCT AND PRICE LIST page similar to the one we have now, but with "LEARN MORE" and "ORDER NOW" buttons for each item.
Updates

Reason: Thanks  for all the designs so far; giving an extra week for extra consideration.

Target Market(s)

Consumers, wedding planners.

Industry/Entity Type

Shopping

Requirements
Must have
• Clean, easy to read design.
Should not have
• No flash animation.

```html
<!DOCTYPE html>
<html lang="en">
<head>
<meta charset="utf-8">
<title>reedcraft studio – Product and Price List</title>
<link rel="stylesheet" href="https://fonts.googleapis.com/css2?family=PT+Sans:wght@400;700&family=Marcellus+SC&family=Alfa+Slab+One&family=Rokkitt:wght@500&family=Tinos&display=swap">
<style>
:root{
  --gold:#b08a2e;
  --gold-light:#c9a445;
  --gold-text:#c29a3a;
  --red:#b60d0d;
  --green:#3aa619;
  --link:#8ecb3a;
  --ink:#f2f2f2;
  --cell:#3d3d3d;
  --cell-alt:#464646;
  --footer:#232323;
}
*{box-sizing:border-box;margin:0;padding:0}
html,body{width:1200px;height:1193px;overflow:hidden;background:#000}
body{position:relative;font-family:"PT Sans",sans-serif;color:var(--ink);
  background:linear-gradient(#9a9a9a 0,#3a3a3a 180px,#000 340px,#000 100%)}
a{color:inherit;text-decoration:none}
.abs{position:absolute}

/* header */
.hero{left:114px;top:0;width:970px;height:330px;border-radius:0 0 6px 6px;
  background:radial-gradient(ellipse at 55% 55%,#c7cfa9 0,#7d9550 25%,#3f6324 55%,#22391a 100%)}
.hero-reflect{left:114px;top:332px;width:970px;height:45px;
  background:linear-gradient(rgba(120,120,100,.55),rgba(0,0,0,0))}
.brand{left:120px;top:4px;width:245px;height:72px;display:flex;align-items:center;gap:10px;
  font-family:"PT Sans",sans-serif;font-size:31px;font-weight:700;color:#fff;line-height:1}
.brand i{display:block;width:16px;height:16px;background:#fff;border-radius:50%;flex:none}
.cartbar{left:700px;top:0;width:384px;height:28px;background:rgba(0,0,0,.55);
  display:flex;align-items:center;padding-left:16px;font-size:12px;font-weight:700}
.cartbar span{font-weight:400}
.btn{display:inline-flex;align-items:center;justify-content:center;background:var(--red);
  color:#fff;font-size:11px;border-radius:4px}
.cartbar .btn{position:absolute;top:4px;height:20px;width:80px}
.topnav{left:368px;top:28px;width:716px;height:36px;background:var(--gold);border-radius:14px 0 0 0;
  display:flex;align-items:center}
.topnav ul{list-style:none;display:flex;padding-left:18px}
.topnav li{font-family:"Marcellus SC",serif;font-size:14px;color:#fff;padding:0 15px;
  border-right:1px solid rgba(255,255,255,.35);line-height:18px}
.topnav li:last-child{border:0}
.search{position:absolute;left:523px;top:8px;width:186px;height:20px;border-radius:10px;
  background:#fff;overflow:hidden}
.search .icon{position:absolute;left:0;top:0;width:34px;height:20px;background:#8a6a1e}
.intro{left:114px;top:135px;width:550px;height:172px;background:rgba(90,90,80,.55);
  border:1px solid rgba(255,255,255,.25);border-radius:6px}
.intro p{position:absolute;font-size:14px;line-height:17px;width:250px}
.intro .btn{position:absolute;width:144px;height:22px;font-size:11px}
.welcome{left:700px;top:64px;width:362px;height:246px;background:rgba(90,90,80,.4);
  border:1px solid rgba(255,255,255,.2);border-radius:0 0 6px 6px;text-align:center}
.welcome h2{font-weight:400;font-size:18px;margin-top:24px}
.welcome .phone{font-size:24px;margin-top:14px}
.welcome p{font-size:14px;line-height:21px;margin-top:32px}
.welcome p em{font-style:normal;color:var(--gold-light)}

/* content */
.section-title{font-size:18px;color:var(--gold-text);border-bottom:1px solid #888;padding-bottom:2px}
.lead{left:144px;top:445px;font-size:12px;line-height:21px}
.lead a{color:var(--link);text-decoration:underline}
.tab{left:308px;top:490px;width:222px;height:24px;background:var(--gold);
  clip-path:polygon(12px 0,210px 0,222px 100%,0 100%);font-size:12px;text-align:center;line-height:24px}
.pricebox{left:110px;top:512px;width:618px;height:474px;border:2px solid var(--gold-light);
  border-radius:6px;background:var(--gold);overflow:hidden}
table{border-collapse:collapse;width:100%;table-layout:fixed;font-size:12px;text-align:center}
th{font-weight:400;font-size:14px;text-align:left;padding:6px 0 0 14px;vertical-align:top;height:44px;
  background:#505050;border-left:1px solid #666;border-bottom:2px solid #777}
th.photo-col{background:var(--gold);border:0}
td{border-left:1px solid #555;background:var(--cell)}
tr:nth-child(even) td{background:var(--cell-alt)}
td.photo{background:var(--gold)!important;border:0}
.thumb{display:block;margin:0 auto;border:2px solid #e6e0cc;border-radius:2px;
  background:linear-gradient(90deg,#d8cfa4,#bca96a,#ece4c4,#a99658,#e0d6ae)}

/* sidebar */
.sidenav{left:803px;top:466px;width:211px;list-style:none;font-size:12px}
.sidenav li{height:20px;line-height:20px;padding-left:18px;border-bottom:1px solid #ddd}
.sidenav li.active{background:var(--gold);position:relative}
.sidenav li.active::before{content:"";position:absolute;left:3px;top:6px;border:4px solid transparent;border-left:6px solid #fff;border-right:0}
.sidenav li.gap{border:0;height:34px}
.promo{left:776px;top:890px;width:253px;height:91px;border:1px solid #bbb;border-radius:4px;
  background:linear-gradient(120deg,#e8e8e8,#5a5a5a 55%,#2a2a2a);text-align:center;
  font-family:"Alfa Slab One",serif;font-size:27px;line-height:30px;color:#fff;padding-top:13px}

/* footer */
.footer{left:0;top:1001px;width:1200px;height:192px;background:var(--footer)}
.footer h3{position:absolute;font-weight:500;font-size:19px;color:var(--gold-text)}
.contact{left:152px;top:1034px;font-size:12px;line-height:18px}
.contact b{font-weight:400;color:var(--green)}
.quote{left:491px;top:1064px;width:255px;font-family:"Tinos",serif;font-size:12px;line-height:15px;color:#e0e0e0}
.quote cite{display:block;margin-top:16px;color:var(--green);font-size:13px}
.qmark{font-family:"Tinos",serif;font-size:34px;color:#eee;line-height:1}
.foot-brand{left:856px;top:1018px;width:174px;height:46px;border-radius:50%;background:#111;
  display:flex;align-items:center;justify-content:center;font-size:18px;font-weight:700;color:#fff}
.copy{left:834px;top:1087px;font-family:"Tinos",serif;font-size:12px;line-height:15px;color:#ddd}
.copy a{color:var(--green);text-decoration:underline}
</style>
</head>
<body>

<div class="abs hero" role="img" aria-label="Photo of a path through a bamboo forest with a bamboo rail bridge"></div>
<div class="abs hero-reflect"></div>
<div class="abs brand"><i></i>reedcraft studio</div>

<div class="abs cartbar">SHOPPING CART:&nbsp;<span>0 Items</span>
  <a class="btn" style="left:183px">View Item</a>
  <a class="btn" style="left:274px">Checkout</a>
</div>

<nav class="abs topnav">
  <ul><li>Home</li><li>Price List</li><li>Blog</li><li>FAQ</li><li>About Us</li><li>Contact Us</li></ul>
  <div class="search"><div class="icon">
    <svg width="34" height="20" viewBox="0 0 34 20"><circle cx="15" cy="8" r="5" fill="none" stroke="#fff" stroke-width="2"/><line x1="19" y1="12" x2="24" y2="16" stroke="#fff" stroke-width="2.5"/></svg>
  </div></div>
</nav>

<div class="abs intro">
  <p style="left:20px;top:27px">Need bamboo poles at a competitive price? Welcome to your one-stop pole shop.</p>
  <p style="left:288px;top:27px">See our complete list of products with prices:</p>
  <a class="btn" style="left:56px;top:104px">Find Out More</a>
  <a class="btn" style="left:339px;top:104px">Clich Here</a>
</div>

<div class="abs welcome">
  <h2>Welcome to your Pole Provider</h2>
  <div class="phone">1 888 412 5093</div>
  <p>Bamboo poles at wholesale prices direct<br>from <em>reedcraft studio</em></p>
</div>

<h2 class="abs section-title" style="left:113px;top:408px;width:612px">Product and Price List</h2>
<div class="abs lead">Click on photo of an item to order.<br>Jump to: <a>Black Poles</a>, <a>Spotted Poles</a>, <a>Bamboo Wedding Arbors.</a></div>

<div class="abs tab">BAMBOO POLES</div>
<div class="abs pricebox">
  <table>
    <colgroup><col style="width:128px"><col style="width:70px"><col style="width:115px"><col style="width:103px"><col style="width:98px"><col></colgroup>
    <tr><th class="photo-col"></th><th>Item #</th><th>Description</th><th>Dimensions</th><th>Pole Price</th><th style="padding-left:12px;line-height:16px">Packing/<br>Carton Price</th></tr>
    <tr style="height:85px"><td class="photo"><span class="thumb" role="img" aria-label="Reed bamboo poles" style="width:92px;height:78px"></span></td><td>C1</td><td>Reed Bamboo</td><td>3x8″ dia. x 60″</td><td>$0.53</td><td>15 poles,<br>$8.00/carton</td></tr>
    <tr style="height:80px"><td class="photo"><span class="thumb" role="img" aria-label="Tonkin bamboo poles" style="width:94px;height:70px"></span></td><td>C3</td><td>Tonkin Bamboo</td><td>7x8″ dia. x 8″</td><td>$1.20</td><td>40 poles,<br>$48.00/carton</td></tr>
    <tr style="height:93px"><td class="photo"><span class="thumb" role="img" aria-label="Huanggu bamboo poles" style="width:94px;height:82px"></span></td><td>C4</td><td>Huanggu Bamboo</td><td>1″ x 8′</td><td>$1.50</td><td>15 poles,<br>$22.50/carton</td></tr>
    <tr style="height:81px"><td class="photo"><span class="thumb" role="img" aria-label="Mao bamboo poles" style="width:96px;height:70px"></span></td><td>T2</td><td>Mao Bamboo</td><td>2″ x 8′</td><td>$6.00</td><td>4 poles,<br>$24.00/carton</td></tr>
    <tr style="height:88px"><td class="photo"><span class="thumb" role="img" aria-label="Large Mao bamboo poles" style="width:96px;height:74px"></span></td><td>M5</td><td>Mao Bamboo</td><td>5″ x 8′</td><td>$20.00</td><td>2 poles,<br>$40.00/carton</td></tr>
  </table>
</div>

<h2 class="abs section-title" style="left:778px;top:408px;width:251px">Navigation</h2>
<ul class="abs sidenav">
  <li class="active">About Bamboo</li><li>Bamboo Carpentry</li><li>Photo Gallery</li><li>All Products and Prices</li><li>Blog</li><li>FAQ</li><li>About Us</li><li>Contact Us</li>
  <li class="gap"></li>
  <li>Wedding Arbors</li><li>Bamboo for Flutes</li><li>Hand Painted Bamboo Poles</li>
  <li class="gap" style="height:21px"></li>
  <li>Black Bamboo</li><li>Spotted Bamboo</li><li>Mao Bamboo</li><li>Reed Bamboo</li><li>Tonkin Bamboo</li><li>Nan Bamboo</li>
</ul>
<div class="abs promo">Promotional<br>Offer</div>

<footer class="abs footer"></footer>
<h3 class="abs" style="left:149px;top:1009px;font-family:'Rokkitt',serif;font-size:20px;font-weight:500;color:var(--gold-text)">Contact Us</h3>
<div class="abs contact">
  <b>Office Hours</b> : 7:30 am - 7:00 pm<br>Monday - Friday.<br>
  <b>Toll Free</b> : 555-5555<br><b>Local</b> : 555-5555<br>
  <b>Office</b>: Harbor Point, CA<br><b>Warehouse</b>: Millbrook, CA<br><br>
  <b>Email</b> : hello@reedcraftstudio.example
</div>
<h3 class="abs" style="left:491px;top:1010px;font-family:'PT Sans',sans-serif;font-size:18px;font-weight:400;color:var(--gold-text)">Testimonials</h3>
<div class="abs qmark" style="left:487px;top:1040px">“</div>
<div class="abs quote">Lorem ipsum dolor sit amety. Lorem ipsum dolor sit amety. Lorem ipsum dolor sit amety. Lorem ipsum dolor sit amety.<cite><i>Client, MM/DD/YY</i></cite></div>
<div class="abs qmark" style="left:717px;top:1102px">”</div>
<div class="abs foot-brand">reedcraft studio</div>
<div class="abs copy">Copyright © 2001 <a>reedcraft studio.</a><br>All Rights Reserved. All Prices USD.</div>

</body>
</html>
```